Stationery Design Project

We are a packaging machinery manufacturer that mainly serve the food industry.
We now require a full set of stationary including name card, envelop, letter paper, and etc. to match our company image. The logo has been awarded in a previous contest which is attached here.
Updates
Project Deadline Extended
Reason: We have extended the deadline. We have adjusted the deadline before launch to avoid confusion but it turns out the new date wasn't implemented by the system. All designers please feel free to submit your design. Thank you!
Target Market(s)
B2B customer, including decision maker in food factories, chemical factories, etc.
Industry/Entity Type
Industry
Colors
Designer to choose colors to be used in the design.
Look and feel
Each slider illustrates characteristics of the customer's brand and the style your logo design should communicate.

```html
<!DOCTYPE html>
<html lang="en">
<head>
<meta charset="utf-8">
<title>Verano Stationery Set</title>
<link rel="stylesheet" href="https://fonts.googleapis.com/css2?family=Roboto:wght@400;500;700&family=Tinos:wght@700&display=swap">
<style>
  :root {
    --green: #136b35;
    --green-soft: #3f8a5a;
    --green-pale: #cfe2d7;
    --grey: #8e9194;
    --grey-light: #e5e6e7;
    --line: #b9bcbe;
    --text: #8a8d90;
    --ink: #1d1d1d;
    --paper: #ffffff;
  }
  * { box-sizing: border-box; margin: 0; padding: 0; }
  html, body { width: 1200px; height: 854px; overflow: hidden; background: var(--paper); }
  body { position: relative; font-family: "Roboto", Arial, sans-serif; color: var(--text); }

  .sheet, .card, .envelope, .envelope-back { position: absolute; background: var(--paper); border: 1px solid var(--line); overflow: hidden; }
  .shape { position: absolute; inset: 0; width: 100%; height: 100%; }

  .brand { position: absolute; display: flex; flex-direction: column; align-items: flex-start; }
  .brand-row { display: flex; align-items: center; gap: 3px; }
  .brand-mark { width: 14px; height: 14px; background: currentColor; }
  .brand-name { font-weight: 700; font-size: 20px; line-height: 1; letter-spacing: 0.5px; }
  .brand-tagline { font-weight: 500; font-size: 5.6px; letter-spacing: 1.3px; margin-top: 2px; white-space: nowrap; }
  .brand--green { color: var(--green); }
  .brand--white { color: var(--paper); }

  .contact { position: absolute; font-size: 5px; line-height: 1.45; color: var(--text); white-space: nowrap; }
  .contact--white { color: var(--paper); }

  .label { position: absolute; font-family: "Tinos", "Times New Roman", serif; font-weight: 700; font-size: 11.5px; color: var(--ink); text-decoration: underline; letter-spacing: 0.2px; white-space: nowrap; }

  .person-name { position: absolute; font-size: 8px; color: var(--green); font-weight: 500; }
  .person-title { position: absolute; font-size: 5px; color: var(--green); }

  .window { position: absolute; border: 1px solid #e58e98; border-radius: 10px; background: var(--paper); }
  .recipient { position: absolute; font-size: 5px; line-height: 1.45; color: var(--ink); }
  .return-line { position: absolute; font-size: 4.5px; color: var(--text); white-space: nowrap; }
  .permit { position: absolute; width: 85px; height: 19px; border: 1px solid var(--ink); background: var(--paper); display: flex; }
  .permit-left { flex: 1; border-right: 1px solid var(--ink); }
  .permit-right { width: 34px; display: flex; align-items: center; justify-content: center; }
  .permit-dot { width: 10px; height: 10px; border-radius: 50%; background: var(--ink); }
</style>
</head>
<body>

<!-- Letterhead 1 -->
<section class="sheet letterhead-1" style="left:134px;top:13px;width:301px;height:425px;">
  <svg class="shape" viewBox="0 0 301 425">
    <rect x="0" y="0" width="301" height="45" fill="var(--green)"/>
    <polygon points="0,350 17,360 17,425 0,425" fill="var(--green-pale)"/>
    <polygon points="17,360 70,403 120,425 17,425" fill="var(--green-pale)"/>
    <polygon points="37,322 58,303 145,392 37,392" fill="var(--grey-light)"/>
  </svg>
  <div class="contact contact--white" style="left:14px;top:5px;">9999, Address Line, Your City,<br>Your State, Zip Code - 100 001.<br>Tel. : 00-11-222-3333 | Fax : 00-11-222-5555<br>Email : yourname@yoursp.com<br>Web : http://www.websitename.com</div>
  <div class="brand brand--white" style="left:206px;top:11px;">
    <div class="brand-row"><span class="brand-mark"></span><span class="brand-name" style="font-size:19px;">VERANO</span></div>
    <span class="brand-tagline" style="font-size:5px;">PACKAGING TECHNOLOGY</span>
  </div>
</section>

<!-- Letterhead 2 -->
<section class="sheet letterhead-2" style="left:448px;top:13px;width:301px;height:425px;">
  <svg class="shape" viewBox="0 0 301 425">
    <polygon points="0,0 24,0 12,12" fill="var(--grey)"/>
    <polygon points="0,10 12,22 24,10 24,425 0,425" fill="var(--green)"/>
    <polygon points="285,350 301,370 301,425 285,425" fill="var(--green-pale)"/>
    <polygon points="190,425 285,405 285,425" fill="var(--green-pale)"/>
    <polygon points="155,392 238,305 285,350 285,392" fill="var(--grey-light)"/>
  </svg>
  <div class="brand brand--green" style="left:184px;top:14px;">
    <div class="brand-row"><span class="brand-mark"></span><span class="brand-name">VERANO</span></div>
    <span class="brand-tagline">PACKAGING TECHNOLOGY</span>
  </div>
  <div class="contact" style="left:30px;top:377px;font-size:4.6px;">9999, Address Line, Your City,<br>Your State, Zip Code - 100 001.<br>Tel. : 00-11-222-3333<br>Fax : 00-11-222-5555<br>Email : yourname@yoursp.com<br>Web : http://www.websitename.com</div>
</section>

<!-- Letterhead 3 -->
<section class="sheet letterhead-3" style="left:766px;top:13px;width:301px;height:425px;">
  <svg class="shape" viewBox="0 0 301 425">
    <polygon points="0,0 213,0 200,14 0,14" fill="var(--green)"/>
    <polygon points="209,0 301,0 301,92" fill="var(--grey)"/>
    <rect x="141" y="385" width="16" height="16" fill="var(--grey-light)"/>
  </svg>
  <div class="brand brand--green" style="left:109px;top:19px;">
    <div class="brand-row"><span class="brand-mark" style="width:11px;height:11px;"></span><span class="brand-name" style="font-size:16px;">VERANO</span></div>
    <span class="brand-tagline" style="font-size:5px;">PACKAGING TECHNOLOGY</span>
  </div>
  <div class="contact" style="left:54px;top:404px;color:var(--green);text-align:center;font-size:4.4px;">9999, Address Line, Your City, Your State, Zip Code - 100 001. Tel. : 00-11-222-3333 Fax : 00-11-222-5555<br>Email : yourname@yoursp.com | Web : http://www.websitename.com</div>
</section>

<div class="label" style="left:209px;top:443px;">LETTERHEAD OPTION 1:</div>
<div class="label" style="left:523px;top:443px;">LETTERHEAD OPTION 2:</div>
<div class="label" style="left:842px;top:443px;">LETTERHEAD OPTION 3:</div>

<!-- Business card 1 -->
<section class="card bcard-1" style="left:322px;top:489px;width:175px;height:107px;">
  <svg class="shape" viewBox="0 0 175 107">
    <rect x="0" y="0" width="40" height="107" fill="var(--green)"/>
    <polygon points="60,20 150,5 175,40 100,60" fill="none" stroke="var(--grey-light)" stroke-width="0.8"/>
  </svg>
  <div class="brand brand--white" style="left:3px;top:94px;transform:rotate(-90deg);transform-origin:0 0;">
    <div class="brand-row"><span class="brand-mark" style="width:13px;height:13px;"></span><span class="brand-name" style="font-size:19px;">VERANO</span></div>
    <span class="brand-tagline" style="font-size:5px;">PACKAGING TECHNOLOGY</span>
  </div>
  <div class="person-name" style="left:51px;top:14px;">Name Surname</div>
  <div class="person-title" style="left:70px;top:25px;">Title</div>
  <div class="contact" style="right:8px;top:59px;text-align:right;">9999, Address Line, Your City,<br>Your State, Zip Code - 100 001.<br>Tel. : 00-11-222-3333 Fax : 00-11-222-5555<br>Email : yourname@yoursp.com<br>Web : http://www.websitename.com</div>
</section>

<!-- Business card 2 front -->
<section class="card bcard-2-front" style="left:516px;top:489px;width:175px;height:107px;border:none;">
  <svg class="shape" viewBox="0 0 175 107">
    <rect width="175" height="107" fill="var(--green)"/>
    <polygon points="25,0 75,0 118,107 50,107" fill="var(--green-soft)" opacity="0.55"/>
    <polygon points="80,0 175,0 175,45 120,75" fill="var(--green-soft)" opacity="0.4"/>
  </svg>
  <div class="brand brand--white" style="left:35px;top:40px;">
    <div class="brand-row"><span class="brand-mark" style="width:15px;height:15px;"></span><span class="brand-name" style="font-size:22px;">VERANO</span></div>
    <span class="brand-tagline" style="font-size:6px;letter-spacing:1.6px;">PACKAGING TECHNOLOGY</span>
  </div>
</section>

<!-- Business card 2 back -->
<section class="card bcard-2-back" style="left:705px;top:489px;width:174px;height:107px;">
  <div class="brand brand--green" style="left:44px;top:10px;">
    <div class="brand-row"><span class="brand-mark" style="width:12px;height:12px;"></span><span class="brand-name" style="font-size:17px;">VERANO</span></div>
    <span class="brand-tagline" style="font-size:5.2px;">PACKAGING TECHNOLOGY</span>
  </div>
  <div class="person-name" style="left:0;right:0;top:46px;text-align:center;">Name Surname</div>
  <div class="person-title" style="left:0;right:0;top:57px;text-align:center;">Title</div>
  <div class="contact" style="left:0;right:0;top:70px;text-align:center;">9999, Address Line, Your City, Your State, Zip Code - 100 001.<br>Tel. : 00-11-222-3333 Fax : 00-11-222-5555<br>Email : yourname@yoursp.com<br>Web : http://www.websitename.com</div>
</section>

<div class="label" style="left:353px;top:603px;">BCARDS OPTION 1:</div>
<div class="label" style="left:643px;top:603px;">BCARDS OPTION 2:</div>

<!-- Envelope 1 -->
<section class="envelope-back" style="left:76px;top:682px;width:320px;height:163px;">
  <svg class="shape" viewBox="0 0 320 163">
    <path d="M256,0 L320,0 L320,138 C300,80 280,40 256,30 Z" fill="var(--green)"/>
  </svg>
</section>
<div class="label" style="left:97px;top:825px;">ENVELOPE OPTION 1:</div>
<section class="envelope envelope-1" style="left:10px;top:640px;width:322px;height:164px;">
  <svg class="shape" viewBox="0 0 322 164">
    <rect x="65" y="0" width="154" height="11" fill="var(--green)"/>
    <polygon points="0,0 54,0 0,68" fill="var(--grey)"/>
  </svg>
  <div class="brand brand--green" style="left:62px;top:15px;">
    <div class="brand-row"><span class="brand-mark"></span><span class="brand-name">VERANO</span></div>
    <span class="brand-tagline">PACKAGING TECHNOLOGY</span>
  </div>
  <div class="return-line" style="left:62px;top:45px;">PO Box 10345, Sample Suburb Centre, Sample Code</div>
  <div class="permit" style="left:221px;top:18px;"><span class="permit-left"></span><span class="permit-right"><span class="permit-dot"></span></span></div>
  <div class="window" style="left:28px;top:70px;width:130px;height:64px;"></div>
  <div class="recipient" style="left:43px;top:91px;">A B Sample<br>123 Sample Envelope Street<br>Sample Address<br>Sampleton 0000</div>
</section>

<!-- Envelope 2 -->
<section class="envelope-back" style="left:472px;top:682px;width:320px;height:163px;">
  <svg class="shape" viewBox="0 0 320 163">
    <path d="M263,0 L320,0 L320,138 C300,80 285,40 263,30 Z" fill="var(--green)"/>
  </svg>
</section>
<div class="label" style="left:493px;top:825px;">ENVELOPE OPTION 2:</div>
<section class="envelope envelope-2" style="left:412px;top:640px;width:323px;height:164px;">
  <svg class="shape" viewBox="0 0 323 164">
    <polygon points="0,0 25,0 25,12 14,22 0,22" fill="var(--green)"/>
    <polygon points="0,22 14,22 25,12 25,0" fill="var(--green)"/>
    <polygon points="0,164 0,148 11,164" fill="var(--grey)"/>
    <polygon points="11,148 25,148 25,164 11,164" fill="var(--grey)"/>
    <polygon points="180,164 248,120 300,140 300,164" fill="#c9d6cc"/>
    <polygon points="195,130 270,30 300,80 300,130" fill="var(--grey-light)"/>
  </svg>
  <div class="brand brand--green" style="left:30px;top:8px;">
    <div class="brand-row"><span class="brand-mark" style="width:12px;height:12px;"></span><span class="brand-name" style="font-size:17px;">VERANO</span></div>
    <span class="brand-tagline" style="font-size:5px;">PACKAGING TECHNOLOGY</span>
  </div>
  <div class="return-line" style="left:30px;top:34px;">PO Box 10345, Sample Suburb Centre, Sample Code</div>
  <div class="permit" style="left:221px;top:16px;"><span class="permit-left"></span><span class="permit-right"><span class="permit-dot"></span></span></div>
  <div class="window" style="left:28px;top:68px;width:130px;height:64px;"></div>
  <div class="recipient" style="left:43px;top:89px;">A B Sample<br>123 Sample Envelope Street<br>Sample Address<br>Sampleton 0000</div>
</section>

<!-- Envelope 3 -->
<section class="envelope-back" style="left:870px;top:682px;width:320px;height:163px;">
  <svg class="shape" viewBox="0 0 320 163">
    <path d="M262,0 L320,0 L320,128 C298,80 284,40 262,30 Z" fill="var(--grey)"/>
  </svg>
</section>
<div class="label" style="left:890px;top:825px;">ENVELOPE OPTION 3:</div>
<section class="envelope envelope-3" style="left:810px;top:640px;width:322px;height:164px;">
  <svg class="shape" viewBox="0 0 322 164">
    <polygon points="0,0 127,0 110,38 0,38" fill="var(--green)"/>
    <polygon points="120,0 136,0 122,19 136,38 120,38 106,19" fill="var(--grey)"/>
  </svg>
  <div class="brand brand--white" style="left:12px;top:10px;">
    <div class="brand-row"><span class="brand-mark" style="width:12px;height:12px;"></span><span class="brand-name" style="font-size:17px;">VERANO</span></div>
    <span class="brand-tagline" style="font-size:5px;">PACKAGING TECHNOLOGY</span>
  </div>
  <div class="return-line" style="left:4px;top:41px;">PO Box 10345, Sample Suburb Centre, Sample Code</div>
  <div class="permit" style="left:221px;top:16px;"><span class="permit-left"></span><span class="permit-right"><span class="permit-dot"></span></span></div>
  <div class="window" style="left:28px;top:68px;width:130px;height:64px;"></div>
  <div class="recipient" style="left:43px;top:89px;">A B Sample<br>123 Sample Envelope Street<br>Sample Address<br>Sampleton 0000</div>
</section>

</body>
</html>
```